Bold Cover needed for a book on Workplace Bullying

I need a book cover design for a book titled, “Iron Silence?” The book recounts my story of bullying in the workplace. It also includes chapters on how readers can minimize/stop workplace bullying, write an effective complaint, and ensure their own mental wellbeing.
I am looking for a bold design using red and black, and possibly distressed lettering. The covers of other books dealing with this subject do not reflect my vision. They are often too childish or look too academic. This book needs to stress the serious nature of a toxic workplace, while appealing to readers experiencing a similar situation. I’d like the cover to reflect the mental anguish associated with workplace bullying (hence the distressed lettering).
I have included a cover that appeals to me (although the coloring is wrong). That said, I am also very happy (and excited) to see your creative input!
On the cover, it should have the following:
Title: Iron Silence?
Subtitle: How the Harbour Works Department Condones Bullying & Ruins Lives
Author: Owen Frick
Other relevant details:
Book size: 5.5” x 8.5”
Back cover will have a blurb, author picture/short bio, and barcode
The blurb on the back cover reads:
Undermining, intimidation and threats
Despite the Department of Harbour Works allegedly holding a zero tolerance for bullying, these behaviours were an everyday occurrence in at least one workplace. Even after a decade of complaints, numerous witnesses and physical proof, the department failed to act. Instead, they looked the other way, allowing one powerful and well-connected individual to end careers and ruin lives.
After being targeted, one teacher resolved to put an end to the abuse experienced by more than fifty employees. His startling story reveals the relentless bullying, mental health ramifications, and insidious tactics used to cover up the corrosive behaviour.
Those who have experienced a toxic workplace will also find much needed support and guidance, intended to minimise suffering and detail a clear way forward. Chapters include dealing with bullying in the workplace, how to lodge a successful complaint, and how to stay sane during any potential legal action.

```html
<!DOCTYPE html>
<html lang="en">
<head>
<meta charset="utf-8">
<title>Iron Silence? — Owen Frick</title>
<link rel="stylesheet" href="https://fonts.googleapis.com/css2?family=Anton&family=Bebas+Neue&display=swap">
<style>
  :root {
    --cover-red: #d92628;
    --ink-black: #000000;
    --paper-white: #ffffff;
  }
  html, body {
    margin: 0;
    padding: 0;
    width: 825px;
    height: 1200px;
    overflow: hidden;
    background: var(--cover-red);
  }
  .book-cover {
    display: block;
    width: 825px;
    height: 1200px;
    background: var(--cover-red);
  }
  .title-main {
    font-family: "Anton", "Bebas Neue", sans-serif;
    fill: var(--ink-black);
  }
  .title-band-word {
    font-family: "Bebas Neue", "Anton", sans-serif;
    fill: var(--paper-white);
    letter-spacing: 4px;
  }
  .subtitle {
    font-family: "Bebas Neue", sans-serif;
    fill: var(--ink-black);
  }
  .author {
    font-family: "Bebas Neue", sans-serif;
    fill: var(--paper-white);
    letter-spacing: 2px;
  }
  .band-fill { fill: var(--cover-red); }
  .band-rule { stroke: var(--ink-black); stroke-width: 12; }
</style>
</head>
<body>
<svg class="book-cover" viewBox="0 0 825 1200" xmlns="http://www.w3.org/2000/svg" aria-label="Iron Silence? How the Harbour Works Department Condones Bullying &amp; Ruins Lives, by Owen Frick">
  <defs>
    <filter id="distressed-ink" x="-5%" y="-5%" width="110%" height="110%">
      <feTurbulence type="fractalNoise" baseFrequency="0.045" numOctaves="3" seed="7" result="noise"/>
      <feColorMatrix in="noise" type="matrix"
        values="0 0 0 0 0  0 0 0 0 0  0 0 0 0 0  0 0 0 -9 5.6" result="holes"/>
      <feComposite in="SourceGraphic" in2="holes" operator="in" result="eroded"/>
      <feTurbulence type="turbulence" baseFrequency="0.02" numOctaves="2" seed="3" result="warp"/>
      <feDisplacementMap in="eroded" in2="warp" scale="6" xChannelSelector="R" yChannelSelector="G"/>
    </filter>
  </defs>

  <!-- Main title word -->
  <text class="title-main" x="170" y="780" font-size="856"
        textLength="490" lengthAdjust="spacingAndGlyphs"
        filter="url(#distressed-ink)">IRON</text>

  <!-- Diagonal band -->
  <g class="title-band">
    <polygon class="band-fill" points="109,531 695,460 718,647 132,718"/>
    <line class="band-rule" x1="109" y1="531" x2="695" y2="460"/>
    <line class="band-rule" x1="132" y1="718" x2="718" y2="647"/>
    <text class="title-band-word" x="413" y="651" font-size="178"
          text-anchor="middle" textLength="520" lengthAdjust="spacingAndGlyphs"
          transform="rotate(-6.9 413 590)">SILENCE</text>
  </g>

  <!-- Subtitle -->
  <text class="subtitle" x="164" y="831" font-size="57"
        textLength="497" lengthAdjust="spacingAndGlyphs">HOW THE HARBOUR WORKS DEPARTMENT</text>
  <text class="subtitle" x="164" y="874" font-size="57"
        textLength="497" lengthAdjust="spacingAndGlyphs">CONDONES BULLYING &amp; RUINS LIVES</text>

  <!-- Author -->
  <text class="author" x="412" y="1055" font-size="56" text-anchor="middle">OWEN FRICK</text>
</svg>
</body>
</html>
```